Flyer Template

I need a flyer template for door knocking on properties. Text Boxes need to be editable, with a header and text body. Footer to be my info. Project to be stylized to match my real estate signs and logo art from past projects

```html
<!DOCTYPE html>
<html lang="en">
<head>
<meta charset="UTF-8">
<title>Home For Sale Flyer</title>
<link href="https://fonts.googleapis.com/css2?family=Montserrat:wght@500;600;700;800&family=Open+Sans:wght@400;500&display=swap" rel="stylesheet">
<style>
  :root {
    --red: #e0061f;
    --black: #111111;
    --white: #ffffff;
    --text: #2a2a2a;
    --rule: #9a9a9a;
    --sky: #dfe6ee;
  }
  * { margin: 0; padding: 0; box-sizing: border-box; }
  html, body { width: 720px; height: 1200px; overflow: hidden; background: var(--white); }
  .flyer { position: relative; width: 720px; height: 1200px; background: var(--white); font-family: "Montserrat", sans-serif; color: var(--black); overflow: hidden; }

  .header-shapes { position: absolute; left: 0; top: 0; width: 720px; height: 310px; }

  .brand { position: absolute; left: 30px; top: 115px; width: 200px; text-align: center; }
  .brand-mark { display: block; width: 34px; height: 34px; margin: 0 auto 16px; background: var(--red); }
  .brand-name { font-weight: 800; font-size: 30px; line-height: 1.02; letter-spacing: 1px; color: var(--black); }

  .headline { position: absolute; right: 36px; top: 40px; text-align: left; }
  .headline-top { display: block; font-weight: 800; font-size: 88px; line-height: 0.95; color: var(--red); letter-spacing: 1px; }
  .headline-bottom { display: block; font-weight: 800; font-size: 66px; line-height: 1.05; color: var(--black); margin-left: -28px; }

  .price { position: absolute; left: 268px; top: 226px; width: 440px; font-weight: 700; font-size: 46px; color: var(--white); letter-spacing: 0.5px; }

  .hero-photo { position: absolute; left: 0; top: 305px; width: 720px; height: 320px; background: linear-gradient(180deg, #e9eef3 0%, #d9dfe4 45%, #bfc6c8 60%, #5fb3cc 80%, #7fae5a 100%); }

  .gallery { position: absolute; left: 42px; top: 545px; width: 276px; }
  .gallery-photo { display: block; width: 276px; height: 146px; border: 4px solid var(--white); box-shadow: 0 2px 6px rgba(0,0,0,0.25); margin-bottom: 18px; }
  .gallery-photo.facade { background: linear-gradient(180deg, #c9ccd6 0%, #e6e6ea 55%, #5c5b60 100%); }
  .gallery-photo.arrival { background: linear-gradient(180deg, #d7dde3 0%, #f1f1f1 50%, #6d9950 100%); }
  .gallery-photo.estate { background: linear-gradient(180deg, #8fb3d8 0%, #d8d2c4 55%, #6c8a4c 100%); }

  .details { position: absolute; left: 352px; top: 640px; width: 340px; }
  .section-title { font-weight: 700; font-size: 19px; color: var(--black); padding-bottom: 6px; border-bottom: 1px solid var(--rule); }
  .section-title .accent { color: var(--red); }
  .about-text { font-family: "Open Sans", sans-serif; font-size: 11.6px; line-height: 1.5; color: var(--text); margin: 14px 0 22px; }
  .features { display: flex; margin-top: 16px; }
  .feature-list { list-style: none; flex: 1; }
  .feature-list + .feature-list { border-left: 1.5px solid var(--red); padding-left: 30px; }
  .feature-list li { display: flex; align-items: center; gap: 10px; font-family: "Open Sans", sans-serif; font-weight: 500; font-size: 17px; line-height: 1.58; color: var(--black); }
  .tick { width: 12px; height: 12px; flex: none; }

  .footer-band { position: absolute; left: 0; top: 1025px; width: 720px; height: 98px; display: flex; }
  .partner { width: 360px; background: var(--black); display: flex; align-items: center; padding-left: 40px; }
  .partner-name { font-weight: 700; font-size: 30px; color: var(--white); letter-spacing: 0.5px; }
  .office-note { flex: 1; background: var(--red); color: var(--white); display: flex; align-items: center; justify-content: center; text-align: center; font-weight: 600; font-size: 19px; line-height: 1.3; letter-spacing: 0.5px; }

  .contact-bar { position: absolute; left: 0; top: 1123px; width: 720px; height: 77px; display: flex; align-items: center; justify-content: center; font-weight: 600; font-size: 15px; color: var(--black); }
  .contact-item { display: flex; align-items: center; gap: 6px; padding: 0 13px; }
  .contact-item + .contact-item { border-left: 1.5px solid var(--red); }
  .contact-icon { width: 13px; height: 13px; }
</style>
</head>
<body>
<main class="flyer">

  <svg class="header-shapes" viewBox="0 0 720 310" aria-hidden="true">
    <polygon points="168,0 196,0 318,132 232,305 204,305 290,132" fill="var(--black)"/>
    <polygon points="262,215 720,215 720,305 212,305" fill="var(--red)"/>
  </svg>

  <div class="brand">
    <span class="brand-mark"></span>
    <p class="brand-name">MARSDEN<br>REALTY</p>
  </div>

  <h1 class="headline">
    <span class="headline-top">HOME</span>
    <span class="headline-bottom">FOR SALE</span>
  </h1>

  <p class="price">Price:$2450,321</p>

  <div class="hero-photo" role="img" aria-label="Modern house with a terrace umbrella and a swimming pool beside a lawn"></div>

  <div class="gallery">
    <div class="gallery-photo facade" role="img" aria-label="Two-storey house with a steep gabled roof"></div>
    <div class="gallery-photo arrival" role="img" aria-label="Couple with suitcases arriving at a modern home"></div>
    <div class="gallery-photo estate" role="img" aria-label="Large classical style mansion among trees"></div>
  </div>

  <section class="details">
    <h2 class="section-title"><span class="accent">ABOUT THE</span> PROPERTY</h2>
    <p class="about-text">Lorem Ipsum is simply dummy text of the printing and typesetting industry. Lorem Ipsum has been the industry's standard dummy text ever since the 1500s, when an unknown printer took a galley of type and scrambled it to make a type specimen book. It has survived not only five centuries, but also the leap into electronic typesetting, remaining essentially unchanged.</p>

    <h2 class="section-title"><span class="accent">PROPERTY</span> FACT &amp; FEATURES</h2>
    <div class="features">
      <ul class="feature-list">
        <li><svg class="tick" viewBox="0 0 12 12"><circle cx="6" cy="6" r="5" fill="none" stroke="var(--red)" stroke-width="1.3"/><path d="M3.5 6.2 5.3 7.8 8.6 4.3" fill="none" stroke="var(--red)" stroke-width="1.3"/></svg>Lorem Ipsum</li>
        <li><svg class="tick" viewBox="0 0 12 12"><circle cx="6" cy="6" r="5" fill="none" stroke="var(--red)" stroke-width="1.3"/><path d="M3.5 6.2 5.3 7.8 8.6 4.3" fill="none" stroke="var(--red)" stroke-width="1.3"/></svg>Lorem Ipsum</li>
        <li><svg class="tick" viewBox="0 0 12 12"><circle cx="6" cy="6" r="5" fill="none" stroke="var(--red)" stroke-width="1.3"/><path d="M3.5 6.2 5.3 7.8 8.6 4.3" fill="none" stroke="var(--red)" stroke-width="1.3"/></svg>Lorem Ipsum</li>
        <li><svg class="tick" viewBox="0 0 12 12"><circle cx="6" cy="6" r="5" fill="none" stroke="var(--red)" stroke-width="1.3"/><path d="M3.5 6.2 5.3 7.8 8.6 4.3" fill="none" stroke="var(--red)" stroke-width="1.3"/></svg>Lorem Ipsum</li>
      </ul>
      <ul class="feature-list">
        <li><svg class="tick" viewBox="0 0 12 12"><circle cx="6" cy="6" r="5" fill="none" stroke="var(--red)" stroke-width="1.3"/><path d="M3.5 6.2 5.3 7.8 8.6 4.3" fill="none" stroke="var(--red)" stroke-width="1.3"/></svg>Lorem Ipsum</li>
        <li><svg class="tick" viewBox="0 0 12 12"><circle cx="6" cy="6" r="5" fill="none" stroke="var(--red)" stroke-width="1.3"/><path d="M3.5 6.2 5.3 7.8 8.6 4.3" fill="none" stroke="var(--red)" stroke-width="1.3"/></svg>Lorem Ipsum</li>
        <li><svg class="tick" viewBox="0 0 12 12"><circle cx="6" cy="6" r="5" fill="none" stroke="var(--red)" stroke-width="1.3"/><path d="M3.5 6.2 5.3 7.8 8.6 4.3" fill="none" stroke="var(--red)" stroke-width="1.3"/></svg>Lorem Ipsum</li>
        <li><svg class="tick" viewBox="0 0 12 12"><circle cx="6" cy="6" r="5" fill="none" stroke="var(--red)" stroke-width="1.3"/><path d="M3.5 6.2 5.3 7.8 8.6 4.3" fill="none" stroke="var(--red)" stroke-width="1.3"/></svg>Lorem Ipsum</li>
      </ul>
    </div>
  </section>

  <footer>
    <div class="footer-band">
      <div class="partner"><span class="partner-name">NORTHGATE PARTNERS</span></div>
      <div class="office-note">EACH OFFICE<br>INDEPENDENTLY OWNED<br>AND OPERATED</div>
    </div>
    <div class="contact-bar">
      <span class="contact-item">
        <svg class="contact-icon" viewBox="0 0 16 16"><path d="M4 1.5 6.3 4.3 4.9 6a9 9 0 0 0 5.1 5.1l1.7-1.4 2.8 2.3-1.3 2.3C7.5 14.3 1.7 8.5 1.7 2.8Z" fill="var(--red)"/></svg>
        555-014-0233
      </span>
      <span class="contact-item">
        <svg class="contact-icon" viewBox="0 0 16 16"><rect x="1" y="3" width="14" height="10" fill="var(--red)"/><path d="M1.5 3.5 8 9l6.5-5.5" fill="none" stroke="var(--white)" stroke-width="1.4"/></svg>
        TMARSDEN@MAILHUB.COM
      </span>
      <span class="contact-item">
        <svg class="contact-icon" viewBox="0 0 16 16"><circle cx="8" cy="8" r="6.5" fill="none" stroke="var(--red)" stroke-width="1.6"/><ellipse cx="8" cy="8" rx="2.8" ry="6.5" fill="none" stroke="var(--red)" stroke-width="1.3"/><path d="M1.5 8h13M2.5 4.8h11M2.5 11.2h11" stroke="var(--red)" stroke-width="1.2"/></svg>
        HOMEFINDERHUB.COM
      </span>
    </div>
  </footer>

</main>
</body>
</html>
```